The bright window tour 2019

I need an improvement of my own design for a speaking tour on shame and mental health. The advertisement will be for social media. I would like someone to remove the background and do something creative and contemporary. My preference is just my head and shoulders.

Target Market(s)

Church pastors and leaders of mental health organisations

Industry/Entity Type

Mental Health

Requirements
Must have
• The same wording as original
• Delete background and replace with something that is simple but funky

```html
<!DOCTYPE html>
<html lang="en">
<head>
<meta charset="utf-8">
<title>The bright window tour 2019 – social post variants</title>
<link rel="stylesheet" href="https://fonts.googleapis.com/css2?family=Questrial&display=swap">
<style>
  :root {
    --page: #ffffff;
    --panel-light: #f4f4f4;
    --panel-shade: #dcdcdc;
    --blue: #4a86f5;
    --blue-deep: #3f6ef0;
    --blue-light: #4fa2f8;
    --grey-blob-top: #a6a6a6;
    --grey-blob-bottom: #bdbdbd;
    --ink: #111111;
    --name: #4a7ef0;
    --portrait-mono-a: #8a8a8a;
    --portrait-mono-b: #1e1e1e;
    --portrait-warm-a: #8b6a52;
    --portrait-warm-b: #18181b;
  }
  * { box-sizing: border-box; margin: 0; padding: 0; }
  html, body {
    width: 1200px;
    height: 656px;
    overflow: hidden;
    background: var(--page);
  }
  .board {
    position: relative;
    width: 1200px;
    height: 656px;
  }
  .post {
    position: absolute;
    width: 505px;
    height: 514px;
    overflow: hidden;
    background: radial-gradient(circle at 55% 40%, var(--panel-light) 0%, var(--panel-light) 35%, var(--panel-shade) 100%);
    font-family: "Questrial", "Century Gothic", sans-serif;
  }
  .post--mono { left: 59px; top: 71px; }
  .post--colour { left: 625px; top: 73px; }
  .post__art {
    position: absolute;
    inset: 0;
    width: 505px;
    height: 514px;
  }
  .brand {
    position: absolute;
    left: 22px;
    top: 160px;
    display: flex;
    align-items: center;
    gap: 6px;
    color: var(--name);
    font-size: 16px;
    letter-spacing: 0.5px;
  }
  .brand__dot {
    width: 10px;
    height: 10px;
    border-radius: 50%;
    background: var(--name);
  }
  .headline {
    position: absolute;
    left: 20px;
    top: 180px;
    color: var(--ink);
    font-weight: 400;
    line-height: 1;
  }
  .headline__lead { display: block; font-size: 38px; }
  .headline__theme { display: block; font-size: 30px; color: var(--blue); margin-top: -3px; }
  .headline__tour { display: block; font-size: 48px; margin-top: -4px; }
</style>
</head>
<body>
<main class="board">

  <section class="post post--mono">
    <svg class="post__art" viewBox="0 0 505 514" aria-hidden="false">
      <defs>
        <linearGradient id="blob-blue-a" x1="0" y1="0" x2="1" y2="1">
          <stop offset="0" stop-color="var(--blue-deep)"/>
          <stop offset="1" stop-color="var(--blue-light)"/>
        </linearGradient>
        <linearGradient id="blob-blue-b" x1="0" y1="1" x2="1" y2="0">
          <stop offset="0" stop-color="var(--blue-deep)"/>
          <stop offset="1" stop-color="var(--blue-light)"/>
        </linearGradient>
        <linearGradient id="blob-grey" x1="0" y1="0" x2="1" y2="1">
          <stop offset="0" stop-color="var(--grey-blob-top)"/>
          <stop offset="1" stop-color="#8e8e8e"/>
        </linearGradient>
        <radialGradient id="dot-grey" cx="0.35" cy="0.35" r="0.7">
          <stop offset="0" stop-color="#d2d2d2"/>
          <stop offset="1" stop-color="#7d7d7d"/>
        </radialGradient>
        <linearGradient id="portrait-mono" x1="0" y1="0" x2="0" y2="1">
          <stop offset="0" stop-color="var(--portrait-mono-a)"/>
          <stop offset="0.55" stop-color="#4a4a4a"/>
          <stop offset="1" stop-color="var(--portrait-mono-b)"/>
        </linearGradient>
      </defs>
      <path class="blob blob--grey" fill="url(#blob-grey)" d="M55 0 H235 C245 25 230 55 195 60 C160 65 135 45 110 60 C85 75 55 75 50 45 C47 25 50 10 55 0Z"/>
      <path class="blob blob--top-right" fill="url(#blob-blue-a)" d="M380 0 H505 V250 C480 275 420 280 395 250 C370 220 390 180 385 150 C380 120 345 100 350 60 C352 35 365 10 380 0Z"/>
      <path class="blob blob--bottom-left" fill="url(#blob-blue-b)" d="M0 330 C20 290 80 275 110 290 C150 310 115 360 145 385 C175 405 185 430 165 455 C135 480 70 470 30 455 C15 450 5 440 0 435Z"/>
      <circle class="dot dot--blue" cx="173" cy="111" r="11" fill="var(--blue)"/>
      <circle class="dot dot--grey" cx="162" cy="345" r="14" fill="url(#dot-grey)"/>
      <g class="cross" stroke="var(--blue)" stroke-width="6" stroke-linecap="round">
        <path d="M286 29 L302 45 M302 29 L286 45"/>
        <path d="M239 290 L253 304 M253 290 L239 304"/>
        <path d="M76 498 L90 512 M90 498 L76 512"/>
      </g>
      <path class="portrait" role="img" aria-label="Black and white cut-out photo of the speaker, head and shoulders, in a black V-neck t-shirt" fill="url(#portrait-mono)" d="M190 514 C195 450 205 380 270 345 C295 335 300 310 290 285 C275 265 265 230 265 180 C265 110 305 70 345 70 C395 70 425 110 420 175 C418 230 405 270 395 290 C390 315 405 335 440 350 C480 365 500 400 505 430 V514Z"/>
      <path class="blob blob--bottom-right" fill="url(#blob-blue-a)" d="M240 514 C265 480 260 440 285 405 C315 365 380 355 430 360 C465 363 490 372 505 380 V514Z"/>
    </svg>
    <div class="brand"><span class="brand__dot"></span><span class="brand__name">ned carver</span></div>
    <h1 class="headline">
      <span class="headline__lead">the</span>
      <span class="headline__theme">bright window</span>
      <span class="headline__tour">tour 2019</span>
    </h1>
  </section>

  <section class="post post--colour">
    <svg class="post__art" viewBox="0 0 505 514">
      <defs>
        <linearGradient id="blob-blue-c" x1="0" y1="0" x2="1" y2="1">
          <stop offset="0" stop-color="var(--blue-deep)"/>
          <stop offset="1" stop-color="var(--blue-light)"/>
        </linearGradient>
        <linearGradient id="blob-blue-d" x1="0" y1="1" x2="1" y2="0">
          <stop offset="0" stop-color="var(--blue-deep)"/>
          <stop offset="1" stop-color="var(--blue-light)"/>
        </linearGradient>
        <linearGradient id="blob-grey-2" x1="0" y1="0" x2="1" y2="1">
          <stop offset="0" stop-color="var(--grey-blob-top)"/>
          <stop offset="1" stop-color="#8e8e8e"/>
        </linearGradient>
        <radialGradient id="dot-grey-2" cx="0.35" cy="0.35" r="0.7">
          <stop offset="0" stop-color="#d2d2d2"/>
          <stop offset="1" stop-color="#7d7d7d"/>
        </radialGradient>
        <linearGradient id="portrait-warm" x1="0" y1="0" x2="0" y2="1">
          <stop offset="0" stop-color="var(--portrait-warm-a)"/>
          <stop offset="0.5" stop-color="#5a4336"/>
          <stop offset="0.7" stop-color="var(--portrait-warm-b)"/>
          <stop offset="1" stop-color="var(--portrait-warm-b)"/>
        </linearGradient>
      </defs>
      <path class="blob blob--grey" fill="url(#blob-grey-2)" d="M55 0 H235 C245 25 230 55 195 60 C160 65 135 45 110 60 C85 75 55 75 50 45 C47 25 50 10 55 0Z"/>
      <path class="blob blob--top-right" fill="url(#blob-blue-c)" d="M380 0 H505 V250 C480 275 420 280 395 250 C370 220 390 180 385 150 C380 120 345 100 350 60 C352 35 365 10 380 0Z"/>
      <path class="blob blob--bottom-left" fill="url(#blob-blue-d)" d="M0 330 C20 290 80 275 110 290 C150 310 115 360 145 385 C175 405 185 430 165 455 C135 480 70 470 30 455 C15 450 5 440 0 435Z"/>
      <circle class="dot dot--blue" cx="173" cy="111" r="11" fill="var(--blue)"/>
      <circle class="dot dot--grey" cx="162" cy="345" r="14" fill="url(#dot-grey-2)"/>
      <g class="cross" stroke="var(--blue)" stroke-width="6" stroke-linecap="round">
        <path d="M286 29 L302 45 M302 29 L286 45"/>
        <path d="M239 290 L253 304 M253 290 L239 304"/>
        <path d="M76 498 L90 512 M90 498 L76 512"/>
      </g>
      <path class="portrait" role="img" aria-label="Full colour cut-out photo of the speaker, head and shoulders, in a black V-neck t-shirt" fill="url(#portrait-warm)" d="M190 514 C195 450 205 380 270 345 C295 335 300 310 290 285 C275 265 265 230 265 180 C265 110 305 70 345 70 C395 70 425 110 420 175 C418 230 405 270 395 290 C390 315 405 335 440 350 C480 365 500 400 505 430 V514Z"/>
      <path class="blob blob--bottom-right" fill="url(#blob-blue-c)" d="M240 514 C265 480 260 440 285 405 C315 365 380 355 430 360 C465 363 490 372 505 380 V514Z"/>
    </svg>
    <div class="brand"><span class="brand__dot"></span><span class="brand__name">ned carver</span></div>
    <h1 class="headline">
      <span class="headline__lead">the</span>
      <span class="headline__theme">bright window</span>
      <span class="headline__tour">tour 2019</span>
    </h1>
  </section>

</main>
</body>
</html>
```